Podcast tile image

Create me a cover image for a new podcast - "Pebble Lantern"
The podcast will be in the following category: business, career, and society and culture.

Target Market(s)

Women

Font styles to use
Sans Serif

Colors

Designer to choose colors to be used in the design.

Requirements
Nice to have
• A heart and a brain image.

```html
<!DOCTYPE html>
<html lang="en">
<head>
<meta charset="utf-8">
<title>Pebble Lantern — Podcast Cover</title>
<link rel="stylesheet" href="https://fonts.googleapis.com/css2?family=Josefin+Sans:ital,wght@0,600;0,700;1,400;1,700&display=swap">
<style>
  :root {
    --bg: #fcdfd3;
    --coral: #f47e54;
    --flame: #f05a28;
    --salmon: #f59e7e;
    --blush: #f8c1aa;
  }
  html, body {
    margin: 0;
    padding: 0;
    width: 1200px;
    height: 1200px;
    overflow: hidden;
    background: var(--bg);
  }
  .cover {
    position: relative;
    width: 1200px;
    height: 1200px;
    background: var(--bg);
    overflow: hidden;
    font-family: "Josefin Sans", "Futura", sans-serif;
  }
  .title-top {
    position: absolute;
    left: 28px;
    top: 34px;
    margin: 0;
    font-weight: 700;
    font-size: 176px;
    line-height: 1;
    letter-spacing: 2px;
    color: var(--coral);
  }
  .title-bar {
    position: absolute;
    left: 67px;
    top: 257px;
    width: 546px;
    height: 60px;
    background: var(--flame);
  }
  .lantern-disc {
    position: absolute;
    left: 105px;
    top: 368px;
  }
  .title-side {
    position: absolute;
    left: 634px;
    top: 660px;
    margin: 0;
    font-weight: 700;
    font-size: 88px;
    line-height: 1;
    color: var(--flame);
    white-space: nowrap;
  }
  .brain-art {
    position: absolute;
    left: 768px;
    top: 28px;
    width: 430px;
    height: 362px;
    border-radius: 46% 54% 48% 52% / 42% 46% 54% 58%;
    background: radial-gradient(circle at 45% 45%, var(--blush), var(--salmon));
    opacity: 0.75;
  }
  .heart-art {
    position: absolute;
    left: 54px;
    top: 876px;
    width: 316px;
    height: 294px;
    border-radius: 46% 46% 50% 50% / 40% 40% 60% 60%;
    background: radial-gradient(circle at 50% 40%, var(--blush), var(--salmon));
    opacity: 0.75;
  }
  .host-line {
    position: absolute;
    left: 413px;
    top: 1012px;
    margin: 0;
    font-size: 58px;
    line-height: 1;
    color: var(--flame);
    white-space: nowrap;
  }
  .host-line .with {
    font-style: italic;
    font-weight: 400;
    margin-right: 36px;
  }
  .host-line .host-name {
    font-style: italic;
    font-weight: 700;
  }
</style>
</head>
<body>
  <main class="cover">
    <h1 class="title-top">PEBBLE</h1>
    <div class="title-bar"></div>

    <svg class="lantern-disc" width="494" height="494" viewBox="0 0 494 494">
      <path fill="var(--coral)" fill-rule="evenodd"
        d="M247 0 A247 247 0 1 0 247.1 0 Z
           M247 99 A148 148 0 1 1 246.9 99 Z"/>
      <circle cx="247" cy="247" r="68" fill="var(--salmon)" role="img" aria-label="Small glossy heart icon"/>
    </svg>

    <p class="title-side">LANTERN.</p>

    <div class="brain-art" role="img" aria-label="Cheerful cartoon brain character in salmon outline"></div>
    <div class="heart-art" role="img" aria-label="Smiling cartoon heart character in salmon outline"></div>

    <p class="host-line"><span class="with">WITH</span><span class="host-name">AUTHOR’S NAME</span></p>
  </main>
</body>
</html>
```